Refinery Service Website (Wholesale) – Luxurious Landing Pages & Industry Hub

We are seeking talented designers to create a luxurious and professional redesign for the wholesale section of our refinery service website, Halvorn KBT. Our current refinery page (https://halvornkbt.example/refinery/) and dental landing page (https://halvornkbt.example/refinery/dental-gold/) provide functional starting points with existing content (words, sections, trust badges, and video placeholders) that must be retained and enhanced with a sophisticated, high-end aesthetic. We serve high-net-worth wholesale clients across industries such as dental practices, mortuaries, estate attorneys, dentists, pawnshops, jewelry stores, and financial advisors. The project includes designing a revamped main wholesale landing page, individual landing pages for each industry with specific sections, and a central hub page to showcase these industries in an SEO-friendly and user-focused way, all while elevating the design to a luxurious standard.

Project Overview
Our refinery service specializes in precious metals and serves a variety of industries through wholesale access. We want the wholesale section of our website to exude sophistication and exclusivity while preserving and enhancing the existing content on our pages. Currently:
• Our refinery page (https://halvornkbt.example/refinery/) provides a basic overview of our services with text, sections, and trust badges, but it lacks visual appeal and a high-end feel.
• Our dental landing page (https://halvornkbt.example/refinery/dental-gold/) targets dental professionals with relevant messaging, sections, and content, but it also feels utilitarian and could benefit from a more elegant design, improved layout, and stronger calls-to-action.
Designers must use the existing words, sections, trust badges, and video placeholders from these pages as a foundation, enhancing them with a luxurious redesign and adding the additional sections specified below. We admire the clean and professional look of https://www.torvelworks.example/, but we aim to elevate our design with a more luxurious and exclusive feel to attract discerning wholesale clients. The redesign will involve:
1 Main Wholesale Landing Page: A complete overhaul of our current refinery page into a luxurious and professional entry point, retaining and enhancing existing content while improving the overall design.
2 Industry-Specific Landing Pages: A dedicated landing page for each of the following industries: dental practices, mortuaries, estate attorneys, dentists, pawnshops, jewelry stores, and financial advisors. Each page must retain and enhance existing content (where applicable) and include specific sections (detailed below) to build trust, provide information, and encourage engagement.
3 Industry Hub Page: A central page that showcases all the industries we serve in a visually appealing and SEO-optimized manner, acting as a gateway to each industry-specific landing page.
Our website is built on WordPress using the Bricks Builder, so design submissions should be provided in HTML, CSS, or as a Figma file for seamless integration. The design must be responsive, visually striking, and optimized for usability across all devices (desktop, tablet, mobile).
Project Scope
We are looking for design submissions that include:
• Main Wholesale Landing Page: A redesigned version of our current refinery page (https://halvornkbt.example/refinery/), transformed into a luxurious and professional entry point for our wholesale services. The new design must retain the existing words, sections, trust badges, and any video placeholders, enhancing them with a high-end aesthetic while improving layout and engagement.
• Industry-Specific Landing Pages: A dedicated landing page for each of the following industries: dental practices, mortuaries, estate attorneys, dentists, pawnshops, jewelry stores, and financial advisors. Each page must:
◦ Retain and enhance existing content (words, sections, trust badges, video placeholders) from pages like our dental landing page (https://halvornkbt.example/refinery/dental-gold/) as a reference, adapting it for each industry. For industries without existing pages, mirror the structure and content style of the dental page while tailoring the messaging and visuals.
◦ Include the following additional sections to enhance functionality and trust:
Trust Badges: A section displaying trust signals (e.g., certifications, accreditations, years in business) to build credibility with visitors. Include placeholders for 4–6 badges/icons, enhancing any existing badges from our current pages.
Testimonials: A section featuring 3–5 customer testimonials with placeholders for quotes, names, and industries (e.g., “Dr. Wesley Brandt, Dental Practice Owner”). If testimonials exist on current pages, enhance their presentation.
Contact Information: A clearly visible section with contact details (e.g., phone number, email, address) styled to match the luxurious aesthetic, improving any existing contact info presentation.
Contact Fillout Form: A user-friendly form for inquiries, including fields for name, email, industry, and message, with a professional design that encourages submissions, enhancing any existing forms.
Shipping Information: A section detailing shipping instructions and processes (e.g., how to send materials for refining), presented clearly and concisely, building on any existing shipping details.
Summary Service Bullet Points: A concise list of 5–7 key services or benefits tailored to the specific industry (e.g., “Fast turnaround for dental scrap” for dental pages, “Secure handling for jewelry inventory” for jewelers), improving any existing bullet points.
Video: Shipping Instructions: A placeholder for a video explaining how to ship materials to us, styled with a play button and a luxurious frame, enhancing any existing video placeholders.
Video: How Our Refinery Works: A placeholder for a video detailing our refining process, designed to match the aesthetic of the page, enhancing any existing video placeholders.
Video: Who We Are: A placeholder for a video introducing our company and values, presented in an elegant and professional manner, enhancing any existing video placeholders.
◦ Include tailored messaging and design elements that resonate with the specific industry (e.g., dental tools and scrap refining benefits for dental pages, elegant estate visuals for attorneys, jewelry displays for jewelers).
◦ Maintain a cohesive design that ties back to the overall luxurious aesthetic of the wholesale section.
• Industry Hub Page: A central hub page that showcases all the industries we serve in an SEO-friendly and visually engaging way. This page should include:
◦ A grid, carousel, or categorized layout featuring each industry with a concise description or tagline (e.g., “Dental Practices: Turn Scrap into Profit”).
◦ Links to each industry-specific landing page for easy navigation.
◦ Design elements that encourage exploration (e.g., hover effects, icons, or visuals representing each industry).
◦ SEO optimization through keyword-rich headings, meta-friendly layouts, and content areas that naturally incorporate industry terms.
• SEO and User Engagement Focus: The design should balance aesthetics with functionality, ensuring that both the hub page and individual landing pages are optimized for search engines (e.g., through clear headings, meta-friendly layouts) and capture user attention with compelling calls-to-action (e.g., “Discover Refinery Solutions for Your Dental Practice” or “Maximize Value for Your Jewelry Inventory”).
Design Requirements
• Aesthetic: Luxurious, elegant, and professional, with a focus on high-net-worth wholesale clients. The current designs (https://halvornkbt.example/refinery/ and https://halvornkbt.example/refinery/dental-gold/) are too basic and functional; we want a high-end look that conveys prestige and trust, using elements like deep golds, silvers, blacks, or whites to evoke luxury while enhancing existing content.
• Typography: Clean, modern, and sophisticated fonts that enhance readability and align with a high-end brand image, improving upon existing typography.
• Imagery: Incorporate placeholders for high-quality imagery relevant to each industry (e.g., dental tools, jewelry displays, legal documents). No stock images required in submissions—just placeholders. Retain and enhance any existing imagery placeholders from our current pages.
• Video Placeholders: Video sections (for shipping instructions, how the refinery works, and who we are) should include placeholders with play buttons and elegant frames that match the luxurious aesthetic, enhancing any existing video placeholders on our current pages.
• Responsiveness: The design must be fully responsive and look great on desktop, tablet, and mobile devices.
• SEO Optimization: The layout should support SEO best practices, such as clear heading structures (H1, H2, etc.), alt-text-friendly image placeholders, and keyword-rich content areas for each industry, building on existing content for SEO purposes.
• Deliverables Format: Submissions should include design files in HTML, CSS, or Figma format, ready for integration into WordPress with Bricks Builder.

Submission Guidelines
We invite designers to submit their concepts based on the following:
• A mockup of the redesigned main wholesale landing page, improving upon our current refinery page (https://halvornkbt.example/refinery/), retaining and enhancing existing words, sections, trust badges, and video placeholders with a luxurious aesthetic.
• A mockup of the industry hub page showcasing all the industries we serve (dental practices, mortuaries, estate attorneys, dentists, pawnshops, jewelry stores, financial advisors).
• At least two examples of industry-specific landing pages (e.g., one for dental practices, improving upon our current dental page (https://halvornkbt.example/refinery/dental-gold/), and one for jewelry stores), showing how the design retains and enhances existing content, incorporates all required sections (trust badges, testimonials, contact info, contact form, shipping info, service bullet points, and video placeholders), and tailors messaging to each audience.
• A brief explanation of your design choices, including how they enhance SEO, tailor messaging for each industry, incorporate and enhance existing content, include the required sections, and align with the luxurious and professional aesthetic we’re seeking.
• Files in HTML, CSS, or Figma format to demonstrate how the design can be implemented.

Judging Criteria
Submissions will be evaluated based on:
• Alignment with the luxurious and professional aesthetic described, significantly improving upon our current designs (https://halvornkbt.example/refinery/ and https://halvornkbt.example/refinery/dental-gold/) while retaining and enhancing existing content.
• Effective retention and enhancement of existing words, sections, trust badges, and video placeholders from our current pages, seamlessly integrating them into the new design.
• Inclusion and effective design of all required sections (trust badges, testimonials, contact info, contact form, shipping info, service bullet points, and video placeholders) on the industry-specific landing pages.
• Creativity and effectiveness in tailoring messaging and visuals for each industry-specific landing page.
• Usability and visual appeal of the industry hub page, including its potential to improve SEO and engage users.
• Suitability for the target audience (high-net-worth wholesale clients in dental, mortuary, legal, pawnshop, jewelry, and financial sectors).
• Compatibility with WordPress and Bricks Builder (based on the format of deliverables).

Additional Notes
• We are open to creative interpretations of “luxury” and encourage designers to think outside the box while maintaining professionalism. Use our current pages as a foundation for content and structure, enhancing and building upon them rather than replacing them entirely.
• The industry hub page should feel intuitive and encourage exploration, potentially using layouts like a grid, carousel, or categorized sections with hover effects.
• Each industry-specific landing page should include a unique value proposition (e.g., “Streamline Your Dental Scrap Refining Process” or “Maximize Value for Your Jewelry Inventory”) to capture attention, building on the clarity of our current dental page but with a more luxurious presentation and all required sections.
• We will provide feedback during the contest and may request revisions from top submissions.

About Us
Halvorn KBT is a leading refinery service provider specializing in precious metals, offering wholesale solutions to a wide range of industries such as dental, jewelry, and legal sectors. Our goal is to create a luxurious online presence that reflects the high value we provide to our clients.
We look forward to seeing your creative designs and how you can bring our vision of a luxurious, industry-focused wholesale section to life!

```html
<!DOCTYPE html>
<html lang="en">
<head>
<meta charset="utf-8">
<title>Halvorn KBT – Wholesale Refinery Pages</title>
<link href="https://fonts.googleapis.com/css2?family=Montserrat:wght@400;500;600;700;800&display=swap" rel="stylesheet">
<style>
:root{
  --gold:#b48a0c;
  --gold-light:#d6b042;
  --ink:#121212;
  --ink-soft:#1e1e1e;
  --paper:#ffffff;
  --card:#f6f4ef;
  --line:#e2ddd0;
  --board:#6d6d6d;
  --text:#1c1c1c;
  --muted:#7a7a7a;
}
*{box-sizing:border-box;margin:0;padding:0}
html,body{width:840px;height:1200px;overflow:hidden}
body{background:var(--board);font-family:'Montserrat',sans-serif;color:var(--text);position:relative}

.frame{position:absolute;overflow:hidden;background:var(--paper)}
.page{position:absolute;left:0;top:0;transform:scale(.257);transform-origin:0 0;background:var(--paper)}
.page.desk{width:510px;--pad:40px;--h1:23px;--h2:15px;--cols:3}
.page.tab{width:308px;--pad:24px;--h1:17px;--h2:12px;--cols:3}
.page.mob{width:152px;--pad:12px;--h1:11px;--h2:9px;--cols:1}

.sec{position:relative;padding:28px var(--pad);overflow:hidden;display:flex;flex-direction:column;gap:12px}
.sec.dark{background:var(--ink);color:#fff}
.sec.center{align-items:center;text-align:center}
.g{color:var(--gold)}
.dark .g{color:var(--gold-light)}

.topbar{height:16px;background:var(--gold);display:flex;justify-content:center;align-items:center;gap:14px;font-size:4px;color:#fff;font-weight:600;white-space:nowrap}
.mob .topbar,.tab .topbar{gap:6px;font-size:3px}
.nav{height:40px;background:var(--ink);display:flex;align-items:center;justify-content:space-between;padding:0 var(--pad)}
.mob .nav,.tab .nav{height:32px}
.brand{display:flex;align-items:center;gap:5px;color:#fff;font-size:6px;font-weight:600;letter-spacing:.12em}
.mob .brand{font-size:4px}
.brand i{width:8px;height:8px;border-radius:50%;border:1px solid #fff;display:block}
.icons{display:flex;gap:8px}
.mob .icons{gap:4px}
.icons i{width:6px;height:6px;border-radius:50%;background:#ddd;display:block}

h1{font-size:var(--h1);font-weight:800;line-height:1.05;letter-spacing:-.01em}
h2{font-size:var(--h2);font-weight:600;line-height:1.2}
.kicker{font-size:5px;color:var(--text)}
.small{font-size:4.5px;line-height:1.5;color:var(--muted)}
.dark .small{color:#bdbdbd}
.mob .small,.mob .kicker{font-size:3.6px}
.btn{display:inline-block;background:var(--gold);color:#fff;font-size:4px;font-weight:600;padding:4px 10px;border-radius:2px;align-self:flex-start;white-space:nowrap}
.center .btn{align-self:center}
.btn.ghost{background:transparent;border:1px solid var(--gold);color:var(--gold)}
.btn-row{display:flex;gap:6px}
.center .btn-row{justify-content:center}
.stars{font-size:5px;color:var(--gold)}
.stars span{color:var(--muted);font-size:3.5px}

.hero-head{display:grid;grid-template-columns:1.2fr 1fr;gap:16px;align-items:start}
.mob .hero-head,.tab .hero-head{grid-template-columns:1fr;text-align:center;justify-items:center;gap:6px}
.mob .hero-head .btn,.tab .hero-head .btn{align-self:center}

.media{position:relative;width:100%;border-radius:6px;background:linear-gradient(135deg,#2a2114 0%,#6b4e12 40%,#caa040 60%,#1b160d 100%);display:flex;align-items:center;justify-content:center;flex-shrink:0}
.media.fire{background:radial-gradient(circle at 50% 60%,#f0b530 0%,#8a4b10 30%,#2b2622 65%,#777 100%)}
.media.plant{background:linear-gradient(160deg,#1d2e44 0%,#3a3630 45%,#d0781e 70%,#222 100%)}
.media.swirl{background:radial-gradient(circle at 30% 40%,#e0b74a 0%,#6e5210 35%,#1a1408 70%)}
.media.warm{background:linear-gradient(135deg,#d9c8b8 0%,#a88b7a 45%,#5a4238 100%)}
.media.teeth{background:radial-gradient(circle at 50% 55%,#e8e8e8 0%,#c9a12e 25%,#2a2a2a 55%,#0c0c0c 100%)}
.play{width:22px;height:22px;border-radius:50%;background:#fff;display:flex;align-items:center;justify-content:center}
.mob .play{width:12px;height:12px}
.play svg{width:45%;height:45%;margin-left:10%}

.stats{display:flex;justify-content:center;gap:20px}
.mob .stats{flex-wrap:wrap;gap:6px}
.tab .stats{gap:10px}
.stat{display:flex;flex-direction:column;align-items:center;gap:3px;font-size:4px;font-weight:700}
.stat i{width:18px;height:18px;border-radius:50%;background:radial-gradient(circle,#d6b042,#6b5208);display:block;border:2px solid #2a2a2a}
.stat i.sq{border-radius:2px;background:#1c1c1c;border:none;width:22px}
.stat span{font-size:3px;font-weight:400;color:var(--muted)}
.partners{display:flex;justify-content:center;gap:18px;align-items:center}
.mob .partners{gap:6px}
.partner{width:44px;height:10px;background:#222;border-radius:1px}
.partner.round{width:22px;height:12px;border-radius:6px;background:#555}
.mob .partner{width:22px;height:6px}

.split{display:grid;grid-template-columns:1fr 1fr;gap:20px;align-items:start}
.mob .split{grid-template-columns:1fr;gap:8px}

.grid{display:grid;grid-template-columns:repeat(var(--cols),1fr);gap:10px;width:100%}
.mob .grid{gap:6px}
.card{background:#fff;color:var(--text);border-radius:3px;padding:10px 6px;display:flex;flex-direction:column;align-items:center;gap:3px;text-align:center;border:1px solid var(--line)}
.card i{width:10px;height:10px;border:1px solid var(--gold);border-radius:2px;display:block}
.card b{font-size:4.5px;font-weight:600}
.card span{font-size:3px;color:var(--muted)}
.card .btn{padding:2px 7px;font-size:3px;align-self:center}
.card.hot{background:linear-gradient(135deg,#2a220e,#8c6c12);color:#fff;border-color:#8c6c12}
.card.hot span{color:#e8d9a8}
.dark .card.tile{background:var(--ink-soft);color:#fff;border-color:#333}
.dark .card.tile span{color:#aaa}

.crest{width:16px;height:10px;align-self:center;flex-shrink:0}

.quotes{display:grid;grid-template-columns:repeat(var(--cols),1fr);gap:10px;width:100%}
.quote{border:1px solid var(--line);border-radius:3px;padding:8px;display:flex;flex-direction:column;gap:4px;text-align:left}
.quote p{font-size:3.2px;line-height:1.5;color:var(--muted)}
.who{display:flex;align-items:center;gap:4px;font-size:3.6px;font-weight:700}
.who i{width:9px;height:9px;border-radius:50%;background:#b7a68a;display:block;flex-shrink:0}
.who i.m{background:#7a3ea1}
.who small{display:block;font-weight:400;font-size:2.8px;color:var(--muted)}

.steps{display:grid;grid-template-columns:repeat(var(--cols),1fr);gap:10px;width:100%}
.step{background:var(--ink-soft);border:1px solid #333;border-radius:3px;padding:8px;display:flex;flex-direction:column;align-items:center;gap:3px;text-align:center}
.step em{font-style:normal;font-size:14px;font-weight:300;color:var(--gold-light)}
.step b{font-size:4px}
.step span{font-size:3px;color:#aaa}

.progress{display:flex;justify-content:space-around;width:100%;font-size:3px;color:var(--muted)}
.progress span{display:flex;flex-direction:column;align-items:center;gap:2px}
.progress i{width:8px;height:8px;border-radius:50%;background:#e6e0d0;display:block}
.progress span:first-child i{background:var(--gold)}
.fields{display:grid;grid-template-columns:repeat(3,1fr);gap:6px 8px;width:100%;text-align:left}
.mob .fields{grid-template-columns:1fr}
.fields.two{grid-template-columns:1fr 1fr}
.field{display:flex;flex-direction:column;gap:2px;font-size:3.4px;font-weight:600}
.field i{height:9px;background:#f1f1f1;border-radius:2px;display:block}
.field.wide{grid-column:1/-1}
.field.wide.tall i{height:22px}

.foot-cols{display:grid;grid-template-columns:repeat(5,1fr);gap:8px;width:100%;text-align:left}
.mob .foot-cols{grid-template-columns:1fr 1fr}
.foot-cols div{display:flex;flex-direction:column;gap:2px;font-size:3px;color:#aaa}
.foot-cols b{color:#fff;font-size:3.6px;margin-bottom:2px}
.news{display:flex;gap:4px;justify-content:center}
.news i{width:40px;height:7px;background:#fff;border-radius:1px;display:block}
.news .btn{padding:1px 8px;font-size:3px}
.foot-brand{font-size:11px;font-weight:500;letter-spacing:.12em;color:#fff;display:flex;align-items:center;gap:8px;white-space:nowrap}
.mob .foot-brand{font-size:5px}
.foot-brand i{width:14px;height:14px;border-radius:50%;border:1px solid #fff;display:block}
.contact-line{display:flex;gap:12px;justify-content:center;font-size:3.4px;color:#ccc;flex-wrap:wrap}
.socials{display:flex;gap:6px;justify-content:center}
.socials i{width:6px;height:6px;background:var(--gold);border-radius:1px;display:block}
.copy{font-size:3px;color:#888}
</style>
</head>
<body>

<!-- ========== Refinery landing – desktop ========== -->
<div class="frame" style="left:82px;top:11px;width:131px;height:1176px">
<div class="page desk" style="height:4576px">
  <div class="topbar"><span>(555) 014-2290</span><span>info@halvornkbt.example</span><span>118 Corbel Ave NE, Brenmoor</span></div>
  <div class="nav"><span class="brand"><i></i>HALVORN KBT</span><span class="icons"><i></i><i></i><i></i><i></i></span></div>

  <section class="sec" style="height:590px;gap:14px">
    <div class="hero-head">
      <div><p class="kicker">Premier Provider for <b>Wholesale</b></p><h1>PRECIOUS METAL<br><span class="g">REFINERIES</span></h1></div>
      <div style="display:flex;flex-direction:column;gap:5px"><p class="small">Your trusted partner for <b>transforming scrap into substantial profit</b>, offering transparency and unmatched expertise.</p><span class="btn">Request a Wholesale Consultation</span><p class="stars">★★★★★ <span>5.0 Rating</span></p></div>
    </div>
    <div class="media" role="img" aria-label="Video: stacked gold bars in a refinery vault" style="height:232px"><span class="play"><svg viewBox="0 0 10 10"><path d="M2 1l7 4-7 4z" fill="#111"/></svg></span></div>
    <p class="small" style="text-align:center;color:var(--text)">We take pride in our timeliness and efficiency<br>and we are proud of what we have achieved</p>
    <div class="stats">
      <div class="stat"><i></i>1,250,000,000+<span>grams refined</span></div>
      <div class="stat"><i></i>100,000+<span>happy clients</span></div>
      <div class="stat"><i></i>5,500 tons<span>metal processed</span></div>
      <div class="stat"><i></i>10+ years<span>in business</span></div>
      <div class="stat"><i class="sq"></i>A+ Rating<span>accredited</span></div>
    </div>
    <p class="small" style="text-align:center;color:var(--text)">And in fact, here are some <b>brands</b> that trust us</p>
    <div class="partners"><span class="partner"></span><span class="partner"></span><span class="partner round"></span></div>
  </section>

  <section class="sec dark" style="height:180px;justify-content:center">
    <div class="split">
      <div style="display:flex;flex-direction:column;gap:6px"><h2>About Our Precious<br><span class="g">Metal Refinery</span></h2><p class="small">Equipped with the latest technology and state of the art assaying equipment used to test each lot of your precious metals, ensuring results are accurate.</p></div>
      <div style="display:flex;flex-direction:column;gap:8px"><p class="small" style="color:#fff;font-size:5px">You will receive an analysis of your metals, certifying the results and giving you peace of mind.</p><span class="btn">Request a Wholesale Consultation</span></div>
    </div>
  </section>

  <section class="sec center" style="height:386px">
    <p class="small">Who we are...</p>
    <h2>About Us: <span class="g">Halvorn KBT<br>Refineries</span></h2>
    <p class="small">Learn more about our journey and the values that drive our commitment to excellence.</p>
    <div class="media plant" role="img" aria-label="Video: refinery worker at the smelting line" style="height:232px"><span class="play"><svg viewBox="0 0 10 10"><path d="M2 1l7 4-7 4z" fill="#111"/></svg></span></div>
  </section>

  <section class="sec dark" style="height:424px">
    <p class="small">Do you want to witness the whole process?</p>
    <h2>We'll offer you - refinery for precious metals<br>that's <span class="g">never behind closed doors</span></h2>
    <div class="media fire" role="img" aria-label="Molten gold poured into a crucible" style="height:232px"></div>
    <div class="split"><p class="small">Here at Halvorn KBT we don't only invite you to witness your lot being melted, we encourage you to watch every step.</p><p class="small">We have a comfortable waiting area with bulletproof walls and windows for you to witness the melting as it happens.</p></div>
  </section>

  <section class="sec" style="height:350px">
    <div class="split"><h2>Check the precious<br>metal <span class="g">refinery in action</span></h2><p class="small">Discover the intricacies of our refining process and our commitment to excellence in the video below.</p></div>
    <div class="media swirl" role="img" aria-label="Video: gold refining in action" style="height:232px"><span class="play"><svg viewBox="0 0 10 10"><path d="M2 1l7 4-7 4z" fill="#111"/></svg></span></div>
  </section>

  <section class="sec dark" style="height:340px">
    <p class="small">We serve various niches and...</p>
    <h2>Here's the range of wholesale <span class="g">industries</span><br>that <span class="g">we serve</span></h2>
    <div class="grid">
      <div class="card"><i></i><b>Dental Practices</b><span>Turn dental scrap into profit</span><span class="btn">Learn More</span></div>
      <div class="card"><i></i><b>Mortuaries</b><span>Reliable and discreet</span><span class="btn">Learn More</span></div>
      <div class="card"><i></i><b>Estate Attorneys</b><span>Maximize estate returns</span><span class="btn">Learn More</span></div>
      <div class="card"><i></i><b>Pawnshops</b><span>Efficient and secure</span><span class="btn">Learn More</span></div>
      <div class="card"><i></i><b>Jewelry Stores</b><span>Expert refining services</span><span class="btn">Learn More</span></div>
      <div class="card"><i></i><b>Financial Advisors</b><span>Asset optimization</span><span class="btn">Learn More</span></div>
    </div>
  </section>

  <section class="sec center" style="height:320px">
    <svg class="crest" viewBox="0 0 16 10"><path d="M1 9h14M3 9l2-7 3 4 3-4 2 7" fill="none" stroke="#b48a0c" stroke-width="1"/></svg>
    <h2>But why choose <span class="g">Halvorn KBT?</span></h2>
    <div class="grid">
      <div class="card"><i></i><b>Price match guarantee</b><span>on all bullion products</span></div>
      <div class="card"><i></i><b>100% insured</b><span>All orders are tracked and insured</span></div>
      <div class="card hot"><i></i><b>Free Shipping</b><span>Orders ship free over $199</span></div>
      <div class="card"><i></i><b>Optimize Your Earnings</b><span>Get the highest payouts with us</span></div>
      <div class="card"><i></i><b>No Middle Man</b><span>Skip the fees, sell direct</span></div>
      <div class="card"><i></i><b>Trust &amp; Reputation</b><span>Fair, transparent, accurate</span></div>
    </div>
  </section>

  <section class="sec dark center" style="height:370px">
    <svg class="crest" viewBox="0 0 16 10"><path d="M1 9h14M3 9l2-7 3 4 3-4 2 7" fill="none" stroke="#d6b042" stroke-width="1"/></svg>
    <h2>You can maximize your earnings with our<br>comprehensive wholesale <span class="g">services</span></h2>
    <div class="grid">
      <div class="card tile"><i></i><b>Transparent Refining</b><span>Watch the process in real time</span></div>
      <div class="card tile"><i></i><b>Accurate Assaying</b><span>State of the art technology</span></div>
      <div class="card tile"><i></i><b>Fast Settlement</b><span>Same day settlements</span></div>
    </div>
    <div class="grid" style="grid-template-columns:repeat(2,1fr);width:66%">
      <div class="card tile"><i></i><b>Secure Handling</b><span>Safety and security first</span></div>
      <div class="card tile"><i></i><b>Expert Consultation</b><span>Guidance from industry experts</span></div>
    </div>
    <span class="btn">Request a Wholesale Consultation</span>
  </section>

  <section class="sec center" style="height:330px">
    <svg class="crest" viewBox="0 0 16 10"><path d="M1 9h14M3 9l2-7 3 4 3-4 2 7" fill="none" stroke="#b48a0c" stroke-width="1"/></svg>
    <h2>Don't take it from us, <b>hear what our previous<br>clients have to say...</b></h2>
    <div class="quotes">
      <div class="quote"><p>First time buying silver today and it was well worth it. The team was quick, friendly and I will be back again.</p><div class="who"><i></i><div>Grant Velloso<small>Dental Practice Owner</small></div></div></div>
      <div class="quote"><p>As a small business owner myself I have to say I was impressed by the honest and thorough quote they provided.</p><div class="who"><i></i><div>Tom Ashby<small>Dental Practice Owner</small></div></div></div>
      <div class="quote"><p>I had several heirlooms that weren't seeing use. They explained the process and paid more than expected.</p><div class="who"><i class="m"></i><div>Marisa Lindqvist<small>Dental Practice Owner</small></div></div></div>
    </div>
    <span class="btn">View All Testimonials</span>
  </section>

  <section class="sec dark center" style="height:386px">
    <p class="small">Curious about how the shipping process works?</p>
    <h2>Here's the easy <span class="g">shipping instructions</span> for your<br>convenience</h2>
    <p class="small">Watch our simple guide to ensure safe and efficient shipping of your precious metals.</p>
    <div class="media" role="img" aria-label="Video: gold scale and shipping guide" style="height:232px"><span class="play"><svg viewBox="0 0 10 10"><path d="M2 1l7 4-7 4z" fill="#111"/></svg></span></div>
  </section>

  <section class="sec center" style="height:404px;gap:10px">
    <svg class="crest" viewBox="0 0 16 10"><path d="M1 9h14M3 9l2-7 3 4 3-4 2 7" fill="none" stroke="#b48a0c" stroke-width="1"/></svg>
    <h2>Fill out <b>Wholesale Registration</b> form</h2>
    <p class="small">If you have questions about our offers or want to order.</p>
    <div class="progress"><span><i></i>Business Details</span><span><i></i>Billing Information</span><span><i></i>Shipping Preference</span><span><i></i>Review and Confirm</span></div>
    <h2 style="font-size:7px;font-weight:500">Input Your Business Details</h2>
    <div class="fields">
      <div class="field">Legal Business Name*<i></i></div><div class="field">Business Type*<i></i></div><div class="field">Tax ID/EIN*<i></i></div>
      <div class="field">Business Email*<i></i></div><div class="field">Date Established*<i></i></div><div class="field">Website*<i></i></div>
      <div class="field">Company Phone*<i></i></div><div class="field">Company Physical Address*<i></i></div><div class="field">City / State / ZIP*<i></i></div>
    </div>
    <span class="btn">Proceed to Billing Info →</span>
  </section>

  <footer class="sec dark center" style="height:440px;gap:12px">
    <div class="foot-cols">
      <div><b>Buying &amp; selling</b><span>Shop Bullion</span><span>Sell Bullion</span><span>Scrap Gold</span><span>Refinery</span></div>
      <div><b>Company</b><span>Leave a Review</span><span>Testimonials</span><span>Refinery Process</span><span>Blog</span></div>
      <div><b>Customer Care</b><span>My Account</span><span>Investment Tools</span><span>Contact Us</span><span>FAQ</span></div>
      <div><b>Legal</b><span>Privacy Policy</span><span>Terms &amp; Conditions</span><span>Shipping Policy</span><span>Return Policy</span></div>
      <div><b>Open Mon–Fri</b><span>10:00 – 5:00 local time</span><span>Halvorn KBT Refineries</span><span>is a proudly independent company</span></div>
    </div>
    <p class="small">Subscribe to our newsletter to be the first to know about special deals and promotions.</p>
    <div class="news"><i></i><span class="btn">Submit</span></div>
    <div class="foot-brand"><i></i>HALVORN KBT REFINERIES</div>
    <p class="small">"Eliminate The Middleman, Get The Maximum Cash for Your Broken or Old Jewelry"</p>
    <div class="contact-line"><span>(555) 014-2290</span><span>info@halvornkbt.example</span><span>118 Corbel Ave NE, Brenmoor</span></div>
    <div class="socials"><i></i><i></i><i></i><i></i><i></i></div>
    <p class="copy">© 2025 All Rights Reserved Halvorn KBT Refineries</p>
  </footer>
</div>
</div>

<!-- ========== Refinery landing – tablet ========== -->
<div class="frame" style="left:242px;top:11px;width:79px;height:973px">
<div class="page tab" style="height:3786px">
  <div class="topbar"><span>(555) 014-2290</span><span>info@halvornkbt.example</span><span>Brenmoor</span></div>
  <div class="nav"><span class="brand"><i></i>HALVORN KBT</span><span class="icons"><i></i><i></i><i></i><i></i></span></div>
  <section class="sec center" style="height:466px">
    <div class="hero-head"><div><p class="kicker">Premier Provider for <b>Wholesale</b></p><h1>PRECIOUS METAL<br><span class="g">REFINERIES</span></h1></div><p class="small">Your trusted partner for <b>transforming scrap into substantial profit</b>, offering transparency.</p><span class="btn">Request a Wholesale Consultation</span><p class="stars">★★★★★ <span>5.0</span></p></div>
    <div class="media" role="img" aria-label="Video: stacked gold bars" style="height:136px"><span class="play"><svg viewBox="0 0 10 10"><path d="M2 1l7 4-7 4z" fill="#111"/></svg></span></div>
    <p class="small" style="color:var(--text)">We take pride in our timeliness and efficiency</p>
    <div class="stats"><div class="stat"><i></i>1.25B+</div><div class="stat"><i></i>100,000+</div><div class="stat"><i></i>5,500</div><div class="stat"><i></i>10+ yrs</div><div class="stat"><i class="sq"></i>A+</div></div>
    <div class="partners"><span class="partner"></span><span class="partner"></span><span class="partner round"></span></div>
  </section>
  <section class="sec dark" style="height:180px;justify-content:center">
    <div class="split"><div style="display:flex;flex-direction:column;gap:5px"><h2>About Our <span class="g">Precious Metal Refinery</span></h2><p class="small">Equipped with the latest technology and assaying equipment.</p></div><div style="display:flex;flex-direction:column;gap:6px"><p class="small" style="color:#fff">You will receive an analysis of your metals, giving you peace of mind.</p><span class="btn">Request a Consultation</span></div></div>
  </section>
  <section class="sec center" style="height:272px">
    <p class="small">Who we are...</p><h2>About Us: <span class="g">Halvorn KBT Refineries</span></h2><p class="small">Learn more about our journey and values.</p>
    <div class="media plant" role="img" aria-label="Video: refinery worker at the smelting line" style="height:130px"><span class="play"><svg viewBox="0 0 10 10"><path d="M2 1l7 4-7 4z" fill="#111"/></svg></span></div>
  </section>
  <section class="sec dark center" style="height:370px">
    <p class="small">Do you want to witness the whole process?</p><h2>We'll offer you - refinery for precious metals that's <span class="g">never behind closed doors</span></h2>
    <div class="media fire" role="img" aria-label="Molten gold poured into a crucible" style="height:186px"></div>
    <div class="split"><p class="small">We invite you to witness your lot being melted.</p><p class="small">A comfortable waiting area with bulletproof windows.</p></div>
  </section>
  <section class="sec" style="height:244px">
    <div class="split"><h2>Check the precious metal <span class="g">refinery in action</span></h2><p class="small">Discover the intricacies of our refining process.</p></div>
    <div class="media swirl" role="img" aria-label="Video: gold refining in action" style="height:130px"><span class="play"><svg viewBox="0 0 10 10"><path d="M2 1l7 4-7 4z" fill="#111"/></svg></span></div>
  </section>
  <section class="sec dark center" style="height:290px">
    <p class="small">We serve various niches and...</p><h2>Here's the range of wholesale <span class="g">industries that we serve</span></h2>
    <div class="grid"><div class="card"><i></i><b>Dental</b><span class="btn">More</span></div><div class="card"><i></i><b>Mortuaries</b><span class="btn">More</span></div><div class="card"><i></i><b>Attorneys</b><span class="btn">More</span></div><div class="card"><i></i><b>Pawnshops</b><span class="btn">More</span></div><div class="card"><i></i><b>Jewelry</b><span class="btn">More</span></div><div class="card"><i></i><b>Advisors</b><span class="btn">More</span></div></div>
  </section>
  <section class="sec center" style="height:280px">
    <h2>But why choose <span class="g">Halvorn KBT?</span></h2>
    <div class="grid"><div class="card"><i></i><b>Price match</b></div><div class="card"><i></i><b>100% insured</b></div><div class="card hot"><i></i><b>Free Shipping</b></div><div class="card"><i></i><b>Optimize Earnings</b></div><div class="card"><i></i><b>No Middle Man</b></div><div class="card"><i></i><b>Trust</b></div></div>
  </section>
  <section class="sec dark center" style="height:330px">
    <h2>You can maximize your earnings with our comprehensive wholesale <span class="g">services</span></h2>
    <div class="grid"><div class="card tile"><i></i><b>Transparent</b></div><div class="card tile"><i></i><b>Assaying</b></div><div class="card tile"><i></i><b>Settlement</b></div></div>
    <div class="grid" style="grid-template-columns:1fr 1fr;width:66%"><div class="card tile"><i></i><b>Secure Handling</b></div><div class="card tile"><i></i><b>Consultation</b></div></div>
    <span class="btn">Request a Wholesale Consultation</span>
  </section>
  <section class="sec center" style="height:360px">
    <h2>Don't take it from us, <b>hear what our previous clients have to say...</b></h2>
    <div class="quotes" style="grid-template-columns:1fr">
      <div class="quote"><p>The team was quick, friendly and fair. Well worth it.</p><div class="who"><i></i><div>Grant Velloso<small>Dental Practice Owner</small></div></div></div>
      <div class="quote"><p>Impressed by the honest and thorough quote they provided.</p><div class="who"><i></i><div>Tom Ashby<small>Dental Practice Owner</small></div></div></div>
      <div class="quote"><p>They explained everything and paid more than expected.</p><div class="who"><i class="m"></i><div>Marisa Lindqvist<small>Dental Practice Owner</small></div></div></div>
    </div>
    <span class="btn">View All Testimonials</span>
  </section>
  <section class="sec center" style="height:270px">
    <p class="small">Curious about how the shipping process works?</p><h2>Here's the easy <span class="g">shipping instructions</span> for your convenience</h2>
    <div class="media" role="img" aria-label="Video: gold scale and shipping guide" style="height:130px"><span class="play"><svg viewBox="0 0 10 10"><path d="M2 1l7 4-7 4z" fill="#111"/></svg></span></div>
  </section>
  <section class="sec center" style="height:320px">
    <h2>Fill out <b>Wholesale Registration</b> form</h2>
    <div class="progress"><span><i></i>Business</span><span><i></i>Billing</span><span><i></i>Shipping</span><span><i></i>Review</span></div>
    <div class="fields"><div class="field">Business Name*<i></i></div><div class="field">Type*<i></i></div><div class="field">Tax ID*<i></i></div><div class="field">Email*<i></i></div><div class="field">Established*<i></i></div><div class="field">Website*<i></i></div><div class="field">Phone*<i></i></div><div class="field">Address*<i></i></div><div class="field">City*<i></i></div></div>
    <span class="btn">Proceed to Billing Info →</span>
  </section>
  <footer class="sec dark center" style="height:350px">
    <div class="foot-cols"><div><b>Buying</b><span>Bullion</span><span>Scrap</span></div><div><b>Company</b><span>Reviews</span><span>Blog</span></div><div><b>Care</b><span>Account</span><span>FAQ</span></div><div><b>Legal</b><span>Privacy</span><span>Terms</span></div><div><b>Open</b><span>Mon–Fri</span></div></div>
    <div class="news"><i></i><span class="btn">Submit</span></div>
    <div class="foot-brand" style="font-size:7px"><i></i>HALVORN KBT REFINERIES</div>
    <div class="contact-line"><span>(555) 014-2290</span><span>info@halvornkbt.example</span></div>
    <div class="socials"><i></i><i></i><i></i><i></i><i></i></div>
    <p class="copy">© 2025 Halvorn KBT Refineries</p>
  </footer>
</div>
</div>

<!-- ========== Refinery landing – mobile ========== -->
<div class="frame" style="left:350px;top:11px;width:39px;height:1107px">
<div class="page mob" style="height:4306px">
  <div class="topbar"><span>(555) 014-2290</span><span>Brenmoor</span></div>
  <div class="nav"><span class="brand"><i></i>HALVORN KBT</span><span class="icons"><i></i><i></i><i></i></span></div>
  <section class="sec center" style="height:372px">
    <div class="hero-head"><p class="kicker">Premier Provider for <b>Wholesale</b></p><h1>PRECIOUS METAL <span class="g">REFINERIES</span></h1><p class="small">Your trusted partner for transforming scrap into profit.</p><span class="btn">Request a Consultation</span><p class="stars">★★★★★</p></div>
    <div class="media" role="img" aria-label="Video: stacked gold bars" style="height:92px"><span class="play"><svg viewBox="0 0 10 10"><path d="M2 1l7 4-7 4z" fill="#111"/></svg></span></div>
    <div class="stats"><div class="stat"><i></i>1.25B+</div><div class="stat"><i></i>100K+</div><div class="stat"><i></i>5,500</div></div>
    <div class="partners"><span class="partner"></span><span class="partner"></span><span class="partner round"></span></div>
  </section>
  <section class="sec dark" style="height:360px">
    <h2>About Our Precious <span class="g">Metal Refinery</span></h2><p class="small">Equipped with the latest technology and assaying equipment used to test each lot of your metals.</p><p class="small" style="color:#fff">You will receive an analysis of your metals.</p><span class="btn">Request a Consultation</span>
    <p class="small" style="text-align:center">Who we are...</p><h2 style="text-align:center">About Us: <span class="g">Halvorn KBT Refineries</span></h2>
  </section>
  <section class="sec center" style="height:176px">
    <div class="media plant" role="img" aria-label="Video: refinery worker at the smelting line" style="height:120px"><span class="play"><svg viewBox="0 0 10 10"><path d="M2 1l7 4-7 4z" fill="#111"/></svg></span></div>
  </section>
  <section class="sec dark center" style="height:304px">
    <p class="small">Witness the whole process?</p><h2>We'll offer you - a refinery that's <span class="g">never behind closed doors</span></h2>
    <div class="media fire" role="img" aria-label="Molten gold poured into a crucible" style="height:100px"></div>
    <p class="small">We invite you to witness your lot being melted, every step.</p>
  </section>
  <section class="sec center" style="height:186px">
    <h2>Check the precious metal <span class="g">refinery in action</span></h2>
    <div class="media swirl" role="img" aria-label="Video: gold refining in action" style="height:70px"><span class="play"><svg viewBox="0 0 10 10"><path d="M2 1l7 4-7 4z" fill="#111"/></svg></span></div>
  </section>
  <section class="sec dark center" style="height:570px">
    <h2>Here's the range of wholesale <span class="g">industries that we serve</span></h2>
    <div class="grid"><div class="card"><i></i><b>Dental Practices</b><span class="btn">Learn More</span></div><div class="card"><i></i><b>Mortuaries</b><span class="btn">Learn More</span></div><div class="card"><i></i><b>Estate Attorneys</b><span class="btn">Learn More</span></div><div class="card"><i></i><b>Pawnshops</b><span class="btn">Learn More</span></div><div class="card"><i></i><b>Jewelry Stores</b><span class="btn">Learn More</span></div><div class="card"><i></i><b>Financial Advisors</b><span class="btn">Learn More</span></div></div>
  </section>
  <section class="sec center" style="height:480px">
    <h2>But why choose <span class="g">Halvorn KBT?</span></h2>
    <div class="grid"><div class="card"><i></i><b>Price match</b></div><div class="card"><i></i><b>100% insured</b></div><div class="card hot"><i></i><b>Free Shipping</b></div><div class="card"><i></i><b>Optimize Earnings</b></div><div class="card"><i></i><b>No Middle Man</b></div><div class="card"><i></i><b>Trust &amp; Reputation</b></div></div>
  </section>
  <section class="sec dark center" style="height:430px">
    <h2>Maximize your earnings with our <span class="g">services</span></h2>
    <div class="grid"><div class="card tile"><i></i><b>Transparent Refining</b></div><div class="card tile"><i></i><b>Accurate Assaying</b></div><div class="card tile"><i></i><b>Fast Settlement</b></div><div class="card tile"><i></i><b>Secure Handling</b></div><div class="card tile"><i></i><b>Expert Consultation</b></div></div>
    <span class="btn">Request a Consultation</span>
  </section>
  <section class="sec center" style="height:390px">
    <h2>Don't take it from us, <b>hear what clients say...</b></h2>
    <div class="quotes"><div class="quote"><p>Quick, friendly and fair. Well worth it.</p><div class="who"><i></i><div>Grant Velloso</div></div></div><div class="quote"><p>An honest and thorough quote.</p><div class="who"><i></i><div>Tom Ashby</div></div></div><div class="quote"><p>Paid more than I expected.</p><div class="who"><i class="m"></i><div>Marisa Lindqvist</div></div></div></div>
    <span class="btn">View All</span>
  </section>
  <section class="sec center" style="height:200px">
    <h2>Here's the easy <span class="g">shipping instructions</span></h2>
    <div class="media" role="img" aria-label="Video: gold scale and shipping guide" style="height:80px"><span class="play"><svg viewBox="0 0 10 10"><path d="M2 1l7 4-7 4z" fill="#111"/></svg></span></div>
  </section>
  <section class="sec center" style="height:470px">
    <h2>Fill out <b>Wholesale Registration</b> form</h2>
    <div class="progress"><span><i></i></span><span><i></i></span><span><i></i></span><span><i></i></span></div>
    <div class="fields"><div class="field">Business Name*<i></i></div><div class="field">Business Type*<i></i></div><div class="field">Tax ID*<i></i></div><div class="field">Email*<i></i></div><div class="field">Established*<i></i></div><div class="field">Website*<i></i></div><div class="field">Phone*<i></i></div><div class="field">Address*<i></i></div><div class="field">City*<i></i></div></div>
    <span class="btn">Proceed →</span>
  </section>
  <footer class="sec dark center" style="height:480px">
    <div class="foot-cols"><div><b>Buying</b><span>Bullion</span><span>Scrap</span><span>Refinery</span></div><div><b>Company</b><span>Reviews</span><span>Blog</span></div><div><b>Care</b><span>Account</span><span>FAQ</span></div><div><b>Legal</b><span>Privacy</span><span>Terms</span><span>Shipping</span></div></div>
    <div class="news"><i></i><span class="btn">Go</span></div>
    <div class="foot-brand"><i></i>HALVORN KBT</div>
    <div class="contact-line"><span>(555) 014-2290</span><span>info@halvornkbt.example</span></div>
    <div class="socials"><i></i><i></i><i></i><i></i></div>
    <p class="copy">© 2025 Halvorn KBT</p>
  </footer>
</div>
</div>

<!-- ========== Dental landing – desktop ========== -->
<div class="frame" style="left:451px;top:11px;width:131px;height:788px">
<div class="page desk" style="height:3066px">
  <div class="topbar"><span>Free shipping &amp; insurance up to three pounds</span><span>Not Local?</span><span>Mail In Your Gold</span></div>
  <div class="nav" style="height:50px"><span class="brand"><i></i>HALVORN KBT</span><span class="icons"><i></i><i></i><i></i><i></i></span></div>
  <section class="sec center" style="height:630px;gap:12px">
    <p class="kicker">Eliminate Middlemen in Selling your Dental Scraps cause...</p>
    <h1>WE BUY <span class="g">DENTAL SCRAP!</span></h1>
    <p class="small">Sell us your gold and silver scrap and get the most competitive payout and peace of mind knowing you are in trusted hands.</p>
    <div class="media warm" role="img" aria-label="Video: dentist inspecting dental gold crowns" style="height:208px"><span class="play"><svg viewBox="0 0 10 10"><path d="M2 1l7 4-7 4z" fill="#c11"/></svg></span></div>
    <div class="btn-row"><span class="btn">Call Us Now</span><span class="btn ghost">Get Directions</span></div>
    <p class="stars">★★★★★ <span>5.0 Rating</span></p>
    <p class="small" style="color:var(--text)">We are proud to be <b>Your most trusted gold buyer</b></p>
    <div class="stats"><div class="stat"><i></i>1,250,000,000+<span>grams refined</span></div><div class="stat"><i></i>100,000+<span>happy clients</span></div><div class="stat"><i></i>4,441,000<span>ounces</span></div><div class="stat"><i></i>10+ years<span>in business</span></div><div class="stat"><i class="sq"></i>A+ Rating<span>accredited</span></div></div>
    <p class="small" style="color:var(--text)">And we <b>work closely</b> with these <b>companies</b> to make sure our customers have the best experience</p>
    <div class="partners"><span class="partner"></span><span class="partner"></span><span class="partner round"></span></div>
  </section>
  <section class="sec dark" style="height:476px">
    <div class="split">
      <div style="display:flex;flex-direction:column;gap:6px"><h2>Sell us your <span class="g">dental scraps</span><br>for <span class="g">instant cash!</span></h2><p class="small">Halvorn KBT is happy to buy your gold! Whether it's gold crowns, scrap or other precious metals, we'll give you top cash for your gold on the spot. We serve customers from Brenmoor to Ashford and beyond.</p></div>
      <div style="display:flex;flex-direction:column;gap:6px"><p class="small" style="color:#fff;font-size:5px">Whether you are local in the Calder Valley, or national, Halvorn KBT will buy your dental scrap!</p><p class="small" style="color:#fff">For those not local, you can mail us your gold and silver items for a quick and easy sale!</p><div class="btn-row"><span class="btn">Get In Touch with Us</span><span class="btn ghost">Mail in your Gold</span></div></div>
    </div>
    <div class="media teeth" role="img" aria-label="Gold and silver dental crowns on black" style="height:234px"></div>
  </section>
  <section class="sec center" style="height:208px;justify-content:center">
    <svg class="crest" viewBox="0 0 16 10"><path d="M1 9h14M3 9l2-7 3 4 3-4 2 7" fill="none" stroke="#b48a0c" stroke-width="1"/></svg>
    <h2>Sell your <span class="g">gold</span> for <span class="g">maximum cash</span>, and<br>get the <span class="g">best payout!</span></h2>
    <p class="small">Repeated business get access to wholesale buy prices, with maximum payouts and fast cash. Family owned and operated, local business in Brenmoor, CV.</p>
    <div class="btn-row"><span class="btn">Get Directions</span><span class="btn ghost">See How It Works →</span></div>
  </section>
  <section class="sec dark" style="height:272px">
    <p class="small">Sell your gold for maximum payout!</p><h2>But <span class="g">how it works?</span> Simple...</h2>
    <div class="steps"><div class="step"><em>01</em><b>Contact us</b><span>Fill out the form to be contacted</span></div><div class="step"><em>02</em><b>Get the items appraised</b><span>Our expert team will test and appraise</span></div><div class="step"><em>03</em><b>Get your cash the same day!</b><span>We offer immediate payment</span></div></div>
    <div class="btn-row"><span class="btn">Call Us Now</span><span class="btn ghost">Not Local? Inquire Now</span></div>
  </section>
  <section class="sec center" style="height:328px">
    <svg class="crest" viewBox="0 0 16 10"><path d="M1 9h14M3 9l2-7 3 4 3-4 2 7" fill="none" stroke="#b48a0c" stroke-width="1"/></svg>
    <h2>We built trust through transparency and here's what<br>our customers have to say...</h2>
    <div class="quotes">
      <div class="quote"><p>First time selling my dental gold today and it was well worth it. Friendly and quick team.</p><div class="who"><i></i><div>Grant Velloso<small>Dental Practice Owner</small></div></div></div>
      <div class="quote"><p>As a small business owner I appreciated the honest and thorough quote they provided.</p><div class="who"><i></i><div>Tom Ashby<small>Dental Practice Owner</small></div></div></div>
      <div class="quote"><p>They explained the process clearly and the payout was more than I expected.</p><div class="who"><i class="m"></i><div>Marisa Lindqvist<small>Dental Practice Owner</small></div></div></div>
    </div>
    <span class="btn">View All Testimonials</span>
  </section>
  <section class="sec dark" style="height:376px">
    <svg class="crest" viewBox="0 0 16 10" style="align-self:flex-start"><path d="M1 9h14M3 9l2-7 3 4 3-4 2 7" fill="none" stroke="#d6b042" stroke-width="1"/></svg>
    <h2>Halvorn KBT Refineries is built on a<br>foundation of trust and transparency, <span style="font-weight:400">and we pride<br>ourselves in excellent customer service and<br>competitive prices.</span></h2>
    <div class="grid"><div class="card"><i></i><b>Price match guarantee</b><span>on all bullion products</span></div><div class="card"><i></i><b>100% insured</b><span>All orders tracked</span></div><div class="card"><i></i><b>Free Shipping</b><span>Orders ship free</span></div><div class="card"><i></i><b>Optimize Your Earnings</b><span>Highest payouts</span></div><div class="card"><i></i><b>No Middle Man</b><span>Sell direct</span></div><div class="card"><i></i><b>Trust &amp; Reputation</b><span>Fair and accurate</span></div></div>
  </section>
  <section class="sec center" style="height:360px">
    <svg class="crest" viewBox="0 0 16 10"><path d="M1 9h14M3 9l2-7 3 4 3-4 2 7" fill="none" stroke="#b48a0c" stroke-width="1"/></svg>
    <h2>Connect <span style="font-weight:400">with Us</span></h2>
    <p class="small">If you have a registered business and are ready to sell your gold, fill out this form to be contacted.</p>
    <div class="fields two" style="width:70%"><div class="field">First Name*<i></i></div><div class="field">Last Name*<i></i></div><div class="field">Email*<i></i></div><div class="field">Phone Number*<i></i></div><div class="field wide tall">What are you looking to sell?*<i></i></div></div>
    <p class="small" style="align-self:flex-start;margin-left:15%">☐ I agree to Terms and Conditions &amp; Privacy Policy</p>
    <span class="btn" style="align-self:flex-start;margin-left:15%">Submit Inquiry</span>
  </section>
  <footer class="sec dark center" style="height:350px">
    <div class="foot-cols"><div><b>Buying &amp; selling</b><span>Shop Bullion</span><span>Sell Bullion</span><span>Scrap Gold</span></div><div><b>Company</b><span>Leave a Review</span><span>Testimonials</span><span>Blog</span></div><div><b>Customer Care</b><span>My Account</span><span>Contact Us</span><span>FAQ</span></div><div><b>Legal</b><span>Privacy Policy</span><span>Terms</span><span>Shipping Policy</span></div><div><b>Open Mon–Fri</b><span>10:00 – 5:00 local time</span></div></div>
    <div class="news"><i></i><span class="btn">Submit</span></div>
    <div class="foot-brand"><i></i>HALVORN KBT REFINERIES</div>
    <div class="contact-line"><span>(555) 014-2290</span><span>info@halvornkbt.example</span><span>118 Corbel Ave NE, Brenmoor</span></div>
    <div class="socials"><i></i><i></i><i></i><i></i><i></i></div>
    <p class="copy">© 2025 All Rights Reserved Halvorn KBT Refineries</p>
  </footer>
</div>
</div>

<!-- ========== Dental landing – tablet ========== -->
<div class="frame" style="left:611px;top:11px;width:79px;height:688px">
<div class="page tab" style="height:2676px">
  <div class="topbar"><span>Free shipping &amp; insurance</span><span>Mail In Your Gold</span></div>
  <div class="nav"><span class="brand"><i></i>HALVORN KBT</span><span class="icons"><i></i><i></i><i></i><i></i></span></div>
  <section class="sec center" style="height:462px">
    <p class="kicker">Eliminate Middlemen in Selling your Dental Scraps</p>
    <h1>WE BUY <span class="g">DENTAL<br>SCRAP!</span></h1>
    <p class="small">Sell us your gold and silver scrap for the most competitive payout.</p>
    <div class="media warm" role="img" aria-label="Video: dentist inspecting dental gold crowns" style="height:146px"><span class="play"><svg viewBox="0 0 10 10"><path d="M2 1l7 4-7 4z" fill="#c11"/></svg></span></div>
    <div class="btn-row"><span class="btn">Call Us Now</span><span class="btn ghost">Get Directions</span></div>
    <div class="stats"><div class="stat"><i></i>1.25B+</div><div class="stat"><i></i>100,000+</div><div class="stat"><i></i>4.4M</div><div class="stat"><i></i>10+</div><div class="stat"><i class="sq"></i>A+</div></div>
    <div class="partners"><span class="partner"></span><span class="partner"></span><span class="partner round"></span></div>
  </section>
  <section class="sec dark" style="height:370px">
    <div class="split"><div style="display:flex;flex-direction:column;gap:5px"><h2>Sell us your <span class="g">dental scraps</span> for <span class="g">instant cash!</span></h2><p class="small">We'll give you top cash for your gold on the spot.</p></div><div style="display:flex;flex-direction:column;gap:5px"><p class="small" style="color:#fff">Local in the Calder Valley or national, we will buy your dental scrap!</p><span class="btn">Get In Touch</span><span class="btn ghost">Mail in your Gold</span></div></div>
    <div class="media teeth" role="img" aria-label="Gold and silver dental crowns on black" style="height:130px"></div>
  </section>
  <section class="sec center" style="height:180px;justify-content:center">
    <h2>Sell your <span class="g">gold</span> for <span class="g">maximum cash</span>, and get the <span class="g">best payout!</span></h2>
    <p class="small">Repeat business gets wholesale buy prices and fast cash.</p>
    <div class="btn-row"><span class="btn">Get Directions</span><span class="btn ghost">How It Works</span></div>
  </section>
  <section class="sec dark center" style="height:260px">
    <h2>But <span class="g">how it works?</span> Simple...</h2>
    <div class="steps"><div class="step"><em>01</em><b>Contact us</b></div><div class="step"><em>02</em><b>Get appraised</b></div><div class="step"><em>03</em><b>Get cash</b></div></div>
    <div class="btn-row"><span class="btn">Call Us Now</span><span class="btn ghost">Not Local?</span></div>
  </section>
  <section class="sec center" style="height:330px">
    <h2>Don't take it from us, <b>hear what our previous clients have to say...</b></h2>
    <div class="quotes" style="grid-template-columns:1fr">
      <div class="quote"><p>Friendly and quick team. Well worth it.</p><div class="who"><i></i><div>Grant Velloso</div></div></div>
      <div class="quote"><p>An honest and thorough quote.</p><div class="who"><i></i><div>Tom Ashby</div></div></div>
      <div class="quote"><p>The payout was more than I expected.</p><div class="who"><i class="m"></i><div>Marisa Lindqvist</div></div></div>
    </div>
    <span class="btn">View All</span>
  </section>
  <section class="sec dark" style="height:340px">
    <h2>Halvorn KBT Refineries is built on a foundation of trust and transparency, <span style="font-weight:400">and we pride ourselves in excellent service.</span></h2>
    <div class="grid"><div class="card"><i></i><b>Price match</b></div><div class="card"><i></i><b>100% insured</b></div><div class="card"><i></i><b>Free Shipping</b></div><div class="card"><i></i><b>Optimize</b></div><div class="card"><i></i><b>No Middle Man</b></div><div class="card"><i></i><b>Trust</b></div></div>
  </section>
  <section class="sec" style="height:290px">
    <h2 style="text-align:center">Connect with Us</h2>
    <p class="small" style="text-align:center">Fill out this form to be contacted.</p>
    <div class="fields two"><div class="field">First Name*<i></i></div><div class="field">Last Name*<i></i></div><div class="field">Email*<i></i></div><div class="field">Phone*<i></i></div><div class="field wide tall">What are you looking to sell?*<i></i></div></div>
    <span class="btn">Submit Inquiry</span>
  </section>
  <footer class="sec dark center" style="height:376px">
    <div class="foot-cols"><div><b>Buying</b><span>Bullion</span><span>Scrap</span></div><div><b>Company</b><span>Reviews</span><span>Blog</span></div><div><b>Care</b><span>Account</span><span>FAQ</span></div><div><b>Legal</b><span>Privacy</span><span>Terms</span></div><div><b>Open</b><span>Mon–Fri</span></div></div>
    <div class="news"><i></i><span class="btn">Submit</span></div>
    <div class="foot-brand" style="font-size:7px"><i></i>HALVORN KBT REFINERIES</div>
    <div class="contact-line"><span>(555) 014-2290</span><span>info@halvornkbt.example</span></div>
    <div class="socials"><i></i><i></i><i></i><i></i><i></i></div>
    <p class="copy">© 2025 Halvorn KBT Refineries</p>
  </footer>
</div>
</div>

<!-- ========== Dental landing – mobile ========== -->
<div class="frame" style="left:718px;top:11px;width:39px;height:773px">
<div class="page mob" style="height:3006px">
  <div class="topbar"><span>Free shipping</span><span>Mail In</span></div>
  <div class="nav"><span class="brand"><i></i>HALVORN KBT</span><span class="icons"><i></i><i></i><i></i></span></div>
  <section class="sec center" style="height:388px">
    <p class="kicker">Eliminate Middlemen in Selling your Dental Scraps</p>
    <h1>WE BUY <span class="g">DENTAL SCRAP!</span></h1>
    <p class="small">Sell us your gold and silver scrap for the best payout.</p>
    <div class="media warm" role="img" aria-label="Video: dentist inspecting dental gold crowns" style="height:78px"><span class="play"><svg viewBox="0 0 10 10"><path d="M2 1l7 4-7 4z" fill="#c11"/></svg></span></div>
    <div class="btn-row"><span class="btn">Call</span><span class="btn ghost">Directions</span></div>
    <div class="stats"><div class="stat"><i></i>1.25B+</div><div class="stat"><i></i>100K+</div><div class="stat"><i></i>10+</div></div>
    <div class="partners"><span class="partner"></span><span class="partner"></span><span class="partner round"></span></div>
  </section>
  <section class="sec dark" style="height:330px">
    <h2>Sell us your <span class="g">dental scraps</span> for <span class="g">instant cash!</span></h2>
    <p class="small">We'll give you top cash for your gold on the spot.</p>
    <p class="small" style="color:#fff">Local or national, we buy your dental scrap!</p>
    <span class="btn">Get In Touch</span><span class="btn ghost">Mail in your Gold</span>
    <div class="media teeth" role="img" aria-label="Gold and silver dental crowns on black" style="height:60px"></div>
  </section>
  <section class="sec center" style="height:200px;justify-content:center">
    <h2>Sell your <span class="g">gold</span> for <span class="g">maximum cash</span>, and get the <span class="g">best payout!</span></h2>
    <p class="small">Wholesale buy prices and fast cash.</p>
    <span class="btn">Get Directions</span><span class="btn ghost">How It Works</span>
  </section>
  <section class="sec dark center" style="height:350px">
    <h2>But <span class="g">how it works?</span> Simple...</h2>
    <div class="steps"><div class="step"><em>01</em><b>Contact us</b></div><div class="step"><em>02</em><b>Get appraised</b></div><div class="step"><em>03</em><b>Get your cash</b></div></div>
    <span class="btn">Call Us Now</span>
  </section>
  <section class="sec center" style="height:400px">
    <h2>Don't take it from us, <b>hear what clients say...</b></h2>
    <div class="quotes"><div class="quote"><p>Friendly, quick and fair.</p><div class="who"><i></i><div>Grant Velloso</div></div></div><div class="quote"><p>Honest and thorough quote.</p><div class="who"><i></i><div>Tom Ashby</div></div></div><div class="quote"><p>Paid more than expected.</p><div class="who"><i class="m"></i><div>Marisa Lindqvist</div></div></div></div>
    <span class="btn">View All</span>
  </section>
  <section class="sec dark" style="height:540px">
    <h2>Halvorn KBT Refineries is built on a foundation of trust and transparency.</h2>
    <div class="grid"><div class="card"><i></i><b>Price match guarantee</b></div><div class="card"><i></i><b>100% insured</b></div><div class="card"><i></i><b>Free Shipping</b></div><div class="card"><i></i><b>Optimize Your Earnings</b></div><div class="card"><i></i><b>No Middle Man</b></div><div class="card"><i></i><b>Trust &amp; Reputation</b></div></div>
  </section>
  <section class="sec" style="height:320px">
    <h2 style="text-align:center">Connect with Us</h2>
    <div class="fields"><div class="field">First Name*<i></i></div><div class="field">Last Name*<i></i></div><div class="field">Email*<i></i></div><div class="field">Phone*<i></i></div><div class="field tall wide">Message*<i></i></div></div>
    <span class="btn">Submit</span>
  </section>
  <footer class="sec dark center" style="height:410px">
    <div class="foot-cols"><div><b>Buying</b><span>Bullion</span><span>Scrap</span></div><div><b>Company</b><span>Reviews</span><span>Blog</span></div><div><b>Care</b><span>Account</span><span>FAQ</span></div><div><b>Legal</b><span>Privacy</span><span>Terms</span></div></div>
    <div class="news"><i></i><span class="btn">Go</span></div>
    <div class="foot-brand"><i></i>HALVORN KBT</div>
    <div class="contact-line"><span>(555) 014-2290</span><span>info@halvornkbt.example</span></div>
    <div class="socials"><i></i><i></i><i></i><i></i></div>
    <p class="copy">© 2025 Halvorn KBT</p>
  </footer>
</div>
</div>

</body>
</html>
```